Tunnel

a graphic meme to be sent to my clients, consisting of a long angular dark tunnel with a bright light at one end; located within the bright light at the end of the tunnel is the number 2021
the illuminated (shiny silver?) 3 dimensional font message running along the left wall of the tunnel is: BE SAFE.!
the smaller font message underneath the graphic is: Best Wishes For a Healthy New Year
Dan Marlowe Mediator (also to be included nearby is a small semi-circle logo of my corporate logo).

Font styles to use
Sans Serif
Other font styles liked:
• 3 dimensional bold lettering for BE SAFE

```html
<!DOCTYPE html>
<html lang="en">
<head>
<meta charset="utf-8">
<title>Be Safe 2021 – Dan Marlowe Mediator</title>
<link rel="stylesheet" href="https://fonts.googleapis.com/css2?family=Questrial&family=Raleway:wght@300&family=Crimson+Pro:ital,wght@0,700;1,400&display=swap">
<style>
  :root {
    --tunnel-dark: #121416;
    --tunnel-mid: #2c3135;
    --tunnel-steel: #4a5258;
    --light-core: #ffffff;
    --light-haze: #c9cbc9;
    --floor-warm: #3b2f27;
    --silver-hi: #ffffff;
    --silver-lo: #b9bcbf;
    --silver-edge: #6d7176;
    --year-ink: #2a2d30;
    --greeting-ink: #ffffff;
    --name-ink: #a9aaab;
    --brand-ink: #d9b84a;
  }
  html, body {
    margin: 0;
    padding: 0;
    overflow: hidden;
    background: var(--tunnel-dark);
  }
  .card {
    position: relative;
    width: 909px;
    height: 1200px;
    overflow: hidden;
    background: var(--tunnel-dark);
  }
  .tunnel-photo {
    position: absolute;
    inset: 0;
    background:
      radial-gradient(ellipse 70px 90px at 670px 660px, var(--light-core) 0%, rgba(255,255,255,0.85) 45%, rgba(255,255,255,0) 100%),
      radial-gradient(ellipse 220px 260px at 660px 650px, rgba(201,203,201,0.55) 0%, rgba(120,110,100,0.25) 45%, rgba(0,0,0,0) 100%),
      radial-gradient(ellipse 620px 700px at 640px 640px, var(--tunnel-mid) 0%, var(--tunnel-steel) 35%, #262a2e 60%, var(--tunnel-dark) 100%);
  }
  .tunnel-photo::after {
    content: "";
    position: absolute;
    left: 0; right: 0; bottom: 0;
    height: 260px;
    background: linear-gradient(to bottom, rgba(59,47,39,0) 0%, var(--floor-warm) 100%);
  }
  .headline {
    position: absolute;
    margin: 0;
    font-family: "Questrial", "Century Gothic", sans-serif;
    font-weight: 400;
    line-height: 1;
  }
  .headline span {
    position: absolute;
    display: block;
    white-space: nowrap;
    color: var(--silver-lo);
    background: linear-gradient(180deg, var(--silver-hi) 0%, #eceeef 55%, var(--silver-lo) 100%);
    -webkit-background-clip: text;
    background-clip: text;
    -webkit-text-fill-color: transparent;
    filter: drop-shadow(-3px 3px 0 var(--silver-edge)) drop-shadow(-2px 4px 4px rgba(0,0,0,0.6));
    transform-origin: left bottom;
  }
  .headline .letter-b {
    left: 70px; top: 250px;
    font-size: 440px;
    transform: skewY(12deg) scaleX(0.68);
  }
  .headline .letter-e {
    left: 268px; top: 400px;
    font-size: 300px;
    transform: skewY(14deg) scaleX(0.58);
  }
  .headline .word-safe {
    left: 407px; top: 520px;
    font-size: 150px;
    transform: skewY(16deg) scaleX(0.42);
  }
  .year {
    position: absolute;
    left: 596px; top: 604px;
    margin: 0;
    font-family: "Questrial", sans-serif;
    font-size: 52px;
    color: var(--year-ink);
    transform: skewY(6deg) scaleX(0.85);
    transform-origin: left bottom;
  }
  .greeting {
    position: absolute;
    left: 520px; top: 838px;
    width: 362px;
    margin: 0;
    text-align: center;
    font-family: "Raleway", sans-serif;
    font-weight: 300;
    font-size: 46px;
    line-height: 45px;
    color: var(--greeting-ink);
  }
  .signature {
    position: absolute;
    left: 310px; top: 1032px;
    margin: 0;
    font-family: "Crimson Pro", serif;
    font-size: 33px;
    color: var(--name-ink);
  }
  .signature .name { font-weight: 700; }
  .signature .role { font-style: italic; font-weight: 400; }
  .firm {
    position: absolute;
    left: 628px; top: 1040px;
    display: flex;
    align-items: center;
    gap: 10px;
    font-family: "Crimson Pro", serif;
    font-weight: 700;
    font-size: 26px;
    color: var(--brand-ink);
  }
  .firm .mark {
    width: 22px; height: 22px;
    border-radius: 50%;
    background: var(--brand-ink);
  }
</style>
</head>
<body>
  <main class="card">
    <div class="tunnel-photo" role="img" aria-label="Photograph of a long curved dark rail tunnel with a bright light at its far end"></div>

    <h1 class="headline" aria-label="Be Safe!">
      <span class="letter-b">B</span>
      <span class="letter-e">E</span>
      <span class="word-safe">SAFE!</span>
    </h1>

    <p class="year">2021</p>

    <p class="greeting">Best Wishes<br>for a Healthy<br>New Year</p>

    <p class="signature"><span class="name">Dan Marlowe</span> <span class="role">Mediator</span></p>

    <div class="firm"><span class="mark"></span>Harlow Pierce</div>
  </main>
</body>
</html>
```